Business Card Design Project

I have just chosen a logo and would now like this designed onto a business card for my hair salon. I would like it to be classy not to busy and have a wow factor when people look at them
Has to Include on card:
Logo Design
And business details below
Kellie-ann Drummond (owner)
0482 736 219
Rdw@vomblet.com.au
71 Willowmere Rise Corvin Cove
Logo is now attached please provide designs
Hair

```html
<!DOCTYPE html>
<html lang="en">
<head>
<meta charset="utf-8">
<title>Velour Hair Atelier – Business Card</title>
<link rel="stylesheet" href="https://fonts.googleapis.com/css2?family=Exo+2:wght@300;400&display=swap">
<style>
  :root {
    --stage: #d9d9dc;
    --card-white: #ffffff;
    --royal: #3a3190;
    --royal-deep: #2a2378;
    --purple: #7a2e9c;
    --magenta: #e0157f;
    --teal: #3bbfc9;
    --teal-soft: #d6f1f3;
  }
  * { margin: 0; padding: 0; box-sizing: border-box; }
  html, body { width: 1200px; height: 900px; overflow: hidden; }
  body {
    background: var(--stage);
    font-family: "Exo 2", sans-serif;
    display: flex;
    flex-direction: column;
    align-items: center;
    justify-content: center;
    gap: 40px;
  }
  .card {
    position: relative;
    width: 700px;
    height: 400px;
    overflow: hidden;
    box-shadow: 0 6px 18px rgba(0,0,0,0.18);
  }

  /* Front face */
  .card--front { background: var(--card-white); }
  .brand {
    position: absolute;
    left: 40px;
    top: 42px;
    display: flex;
    align-items: center;
    gap: 10px;
    color: var(--magenta);
    font-weight: 400;
    font-size: 24px;
    letter-spacing: 1px;
  }
  .brand__dot {
    width: 12px; height: 12px;
    border-radius: 50%;
    background: var(--magenta);
  }
  .owner-band {
    position: absolute;
    right: 0;
    top: 130px;
    width: 470px;
    height: 64px;
    background: linear-gradient(90deg, rgba(255,255,255,0) 0%, var(--teal-soft) 70%, var(--teal-soft) 100%);
    text-align: right;
    padding: 8px 22px 0 0;
  }
  .owner-band__name {
    color: var(--purple);
    font-size: 27px;
    font-weight: 400;
    line-height: 1;
  }
  .owner-band__role {
    color: var(--teal);
    font-size: 18px;
    line-height: 1;
    margin-top: 2px;
  }
  .rule {
    position: absolute;
    height: 3px;
  }
  .rule--magenta { right: 60px; top: 196px; width: 250px; background: var(--magenta); }
  .rule--teal { right: 0; top: 190px; width: 130px; background: var(--teal); }

  .contact {
    position: absolute;
    left: 40px;
    bottom: 48px;
    padding-left: 22px;
    border-left: 7px solid var(--magenta);
    color: var(--purple);
    font-weight: 300;
    font-size: 31px;
    line-height: 1.22;
  }

  /* Back face */
  .card--back {
    background: radial-gradient(ellipse at 45% 40%, var(--royal) 0%, var(--royal-deep) 100%);
    display: flex;
    flex-direction: column;
    align-items: center;
    justify-content: center;
    color: #ffffff;
    font-weight: 400;
  }
  .back-brand__name {
    font-size: 92px;
    letter-spacing: 6px;
    line-height: 1;
  }
  .back-brand__line {
    font-size: 46px;
    letter-spacing: 4px;
    margin-top: 8px;
  }
</style>
</head>
<body>
  <section class="card card--front" aria-label="Card front">
    <div class="brand"><span class="brand__dot"></span>VELOUR HAIR ATELIER</div>
    <div class="owner-band">
      <div class="owner-band__name">Kellie-ann Drummond</div>
      <div class="owner-band__role">owner</div>
    </div>
    <div class="rule rule--teal"></div>
    <div class="rule rule--magenta"></div>
    <div class="contact">
      <div>0482 736 219</div>
      <div>Rdw@vomblet.com.au</div>
      <div>71 Willowmere Rise Corvin Cove</div>
    </div>
  </section>

  <section class="card card--back" aria-label="Card back">
    <div class="back-brand__name">VELOUR</div>
    <div class="back-brand__line">HAIR ATELIER</div>
  </section>
</body>
</html>
```